Website for a company offering full serivce charging solutions for electric cars

The company "vorn-werk" (english: "front-works") offering all-in-one-solutions for charging infrastructure for electric mobility.

There are four products:
1- Wallboxes for single-family homes
2- Solutions for property devloper/-management for property parking space
3- All-in-one-charging solution for municipalities/communities
4- Solutions for tourism/hotels/holiday appartments

The Website structure:
1. Main Page
2.1. Product Page Single Homes
2.2. Product Page Property Management / Parking
2.3. Product Page Municipality
2.4. Product Page Tourism
3. Contact Form / Request for information
4. Imprint / Legal

The Website should be built on Wordpress with a powerful possibility to simply add/modify specific landing pages.

We would like you to implement the website later and also maintain it if possible, but we would be able to do minor modifications by ourselfs (for A/B-Testing)

The website should be clear and simple, easy to understand.
Target group is mainly B2C without deeper knowledge of that topic.

It should suggest, that we will provide a very simple way to get the charging infrastructure done.

We need a contact form, maybe we will use Leadmill later.

Attached you will find a draft of the main page and a landing page (for 2.2) - it is just the content, please ignore the design. We would love to let you create a suitable design.
Also you will find some drafts a bit different for the same story.

I added also a few stock photos, but they don't need to be used! If you have better ideas, you are welcome!

Charging/Electric mobility

Sans Serif

• Based on Wordpress, and the designer should be able to implement it on Wordpress on a later step

```html
<!DOCTYPE html>
<html lang="de">
<head>
<meta charset="utf-8">
<title>vorn-werk.de – Ladelösungen</title>
<link href="https://fonts.googleapis.com/css2?family=Ubuntu:wght@400;500;700&family=Open+Sans:wght@400;600&display=swap" rel="stylesheet">
<style>
:root{
  --purple:#8e44c0;
  --violet:#7a4fbf;
  --magenta:#b4179a;
  --plum:#a0239e;
  --ink:#1d1d1d;
  --text:#333;
  --tint:#efe7ef;
  --navy:#151a2b;
  --navy-dark:#0f1320;
  --white:#fff;
}
*{box-sizing:border-box;margin:0;padding:0}
html,body{width:1200px;height:2937px;overflow:hidden}
body{font-family:"Open Sans",sans-serif;color:var(--text);background:var(--white)}
.site-header{height:88px;display:flex;align-items:center;justify-content:space-between;padding:0 111px}
.brand{display:flex;align-items:center;gap:10px;font-family:"Ubuntu",sans-serif;font-size:30px;font-weight:500;color:var(--ink)}
.brand-dot{width:18px;height:18px;border-radius:50%;background:var(--magenta)}
.main-nav{display:flex;gap:38px;font-size:19px;color:var(--ink)}
.main-nav a{color:inherit;text-decoration:none;position:relative}
.main-nav a.active{color:var(--purple)}
.main-nav a.active svg{position:absolute;left:50%;top:-26px;transform:translateX(-50%)}
.hero{position:relative;height:532px;background:linear-gradient(135deg,#8a8f98 0%,#5c5f66 35%,#7a1f25 60%,#3d3f45 100%);display:flex;align-items:center;justify-content:center}
.hero h1{font-family:"Ubuntu",sans-serif;font-weight:500;font-size:68px;line-height:78px;color:var(--white);text-align:center;margin-top:-30px}
.hero-arrow{position:absolute;top:242px;width:48px;height:48px;border:2px solid rgba(255,255,255,.8);border-radius:50%;display:flex;align-items:center;justify-content:center}
.hero-arrow.prev{left:31px}.hero-arrow.next{right:31px}
.hero-down{position:absolute;bottom:36px;left:50%;transform:translateX(-50%)}
.partner{height:642px;padding:80px 111px 0;display:flex;justify-content:space-between}
.partner-text{width:510px}
.section-title{font-family:"Ubuntu",sans-serif;font-weight:500;font-size:39px;color:var(--purple)}
.partner .section-title{display:inline-block;padding-bottom:12px;border-bottom:3px solid var(--purple);width:408px}
.lead{font-size:18px;line-height:31px;color:var(--ink);margin:28px 0 14px}
.partner-text p.body{font-size:16.5px;line-height:30px;text-align:justify;margin-bottom:14px}
.hl{color:var(--magenta);font-weight:600}
.partner-visual{margin-top:167px;width:382px;height:374px;border-left:8px solid var(--violet);border-bottom:8px solid var(--magenta);position:relative}
.partner-visual .photo{position:absolute;inset:0 0 0 0;background:radial-gradient(circle at 65% 45%,#3b6cff 0%,#9fb8ff 30%,#e6e8ee 60%,#c9ccd3 100%);box-shadow:0 4px 14px rgba(0,0,0,.2)}
.solutions{background:var(--tint);height:1460px;padding-top:46px;text-align:center}
.solutions .section-title{display:inline-block;padding-bottom:18px;border-bottom:3px solid var(--purple);width:168px}
.cards{display:flex;gap:20px;justify-content:center;margin-top:60px;text-align:left}
.card{width:313px;height:1203px;background:#fafafa;border-radius:4px;box-shadow:0 2px 8px rgba(0,0,0,.06)}
.card-head{height:132px;border-radius:4px 4px 0 0;display:flex;flex-direction:column;align-items:center;justify-content:center;color:var(--white);font-family:"Ubuntu",sans-serif;font-weight:500;font-size:21px}
.card-head::after{content:"";width:72px;height:2px;background:var(--white);margin-top:14px}
.card.private .card-head{background:var(--plum)}
.card.business .card-head{background:linear-gradient(135deg,#8b47b9,#6a56b8)}
.card.municipal .card-head{background:linear-gradient(135deg,#a31f9f,#8b38aa)}
.features{list-style:none;padding:30px 22px 0 24px}
.features li{position:relative;padding-left:28px;font-size:17px;line-height:26px;color:var(--text);margin-bottom:20px}
.features li::before{content:"";position:absolute;left:0;top:6px;width:10px;height:10px;border:2px solid var(--magenta);border-radius:50%}
.features li::after{content:"";position:absolute;left:4px;top:9px;width:3px;height:5px;border:solid var(--magenta);border-width:0 2px 2px 0;transform:rotate(45deg)}
.business .features li::before{border-color:var(--violet)}
.business .features li::after{border-color:var(--violet)}
.business .features li.sub::before{width:0;height:0;border:none;border-left:6px solid var(--violet);border-top:5px solid transparent;border-bottom:5px solid transparent;border-radius:0;left:2px}
.business .features li.sub::after{display:none}
.business .features li.sub{margin-bottom:16px}
.site-footer{background:var(--navy);height:170px;padding:36px 111px 0;display:flex;justify-content:space-between;align-items:flex-end}
.footer-brand{font-family:"Ubuntu",sans-serif;font-weight:500;font-size:31px;color:var(--white);margin-bottom:24px;display:flex;align-items:center;gap:10px}
.footer-right{display:flex;flex-direction:column;align-items:flex-end;gap:18px;margin-bottom:26px}
.socials{display:flex;gap:8px}
.socials span{width:38px;height:38px;border-radius:50%;background:var(--magenta);border:2px solid var(--white)}
.footer-nav{display:flex;gap:27px;font-size:18px;color:var(--white)}
.copyright{background:var(--navy-dark);height:45px;display:flex;align-items:center;justify-content:center;color:#ddd;font-size:16px}
</style>
</head>
<body>
<header class="site-header">
  <div class="brand"><span class="brand-dot"></span>vorn-werk.de</div>
  <nav class="main-nav">
    <a class="active" href="#">
      <svg width="12" height="16" viewBox="0 0 12 16"><path d="M7 0 1 9h4l-1 7 7-10H7z" fill="#8e44c0"/></svg>Lösungen</a>
    <a href="#">Unternehmen</a><a href="#">Services</a><a href="#">Karriere</a><a href="#">Kontakt</a>
  </nav>
</header>

<section class="hero" role="img" aria-label="Foto: Mann mit Smartphone lehnt an einem roten Elektroauto, das geladen wird">
  <span class="hero-arrow prev"><svg width="14" height="14" viewBox="0 0 14 14"><path d="M9 2 4 7l5 5" stroke="#fff" stroke-width="2" fill="none"/></svg></span>
  <h1>Willkommen zu<br>vorn-werk.de</h1>
  <span class="hero-arrow next"><svg width="14" height="14" viewBox="0 0 14 14"><path d="M5 2l5 5-5 5" stroke="#fff" stroke-width="2" fill="none"/></svg></span>
  <svg class="hero-down" width="20" height="34" viewBox="0 0 20 34"><path d="M10 0v31M2 23l8 9 8-9" stroke="#fff" stroke-width="2" fill="none"/></svg>
</section>

<section class="partner">
  <div class="partner-text">
    <h2 class="section-title">vorn-werk ist Ihr Partner</h2>
    <p class="lead">wenn das Laden nicht nur einfach, sondern die Umsetzung auch aus einer Hand kommen soll</p>
    <p class="body">Wir bieten Lösungen sowohl für <span class="hl">Privatkunden, Geschäftskunden</span> als auch <span class="hl">Kommunen</span> an, die schnell, fair und ohne Eigenleistung zu einer smarten Ladelösung für E-Fahrzeuge kommen möchten.</p>
    <p class="body">Von der Beratung, über die Installation, Inbetriebnahme bis zur Abrechnung und Wartung bekommen Sie bei vorn-werk alles aus einer Hand. Auf Wunsch vermieten wir auch die Ladetechnik und übernehmen im gewerblichen Bereich die direkte Abrechnung mit dem Nutzer. Für Kommunen bieten wir den kostenfreien Full-Service an und beteiligen die Gemeinden an der Nutzung der Infrastruktur.</p>
  </div>
  <div class="partner-visual"><div class="photo" role="img" aria-label="Foto: Ladestecker in einer blau beleuchteten Ladebuchse"></div></div>
</section>

<section class="solutions">
  <h2 class="section-title">Lösungen</h2>
  <div class="cards">
    <article class="card private">
      <div class="card-head">als Privatkunde</div>
      <ul class="features">
        <li>Bestandsanalyse mit umfangreicher Beratung über die Möglichkeiten der Umsetzung</li>
        <li>Prüfung und Übernahme der Anmeldung verfügbarer Fördermöglichkeiten</li>
        <li>Auswahl an smarten Wallbox Lösungen, passend für Ihr Fahrzeug und Ihre Bedürfnisse</li>
        <li>Installation inkl. aller notwendigen Materialien und Tätigkeiten (Durchbrüche, Erdarbeiten, etc.)</li>
        <li>Inbetriebnahme und Einweisung in die Ladetechnik</li>
        <li>Jährlich technische Wartung nach DGUV3</li>
        <li>Reparaturservice, unter Berücksichtigung der geltenden Garantie Ansprüche</li>
      </ul>
    </article>
    <article class="card business">
      <div class="card-head">als Geschäftskunde</div>
      <ul class="features">
        <li>Durchführung einer individuellen Bedarfsanalyse inkl. Ermittlung der Anforderungen für:</li>
        <li class="sub">Haus- und Immobilienverwaltungen</li>
        <li class="sub">Dienstleistungs- und Handelsunternehmen</li>
        <li class="sub">Hotel und Beherbergungsbetriebe</li>
        <li class="sub">Parkraum- und Parkhausbetreiber</li>
        <li class="sub">Tourismus, Sport- und Freizeiteinrichtungen</li>
        <li>Prüfung und Übernahme der Anmeldung verfügbarer Fördermöglichkeiten</li>
        <li>Auswahl an smarten Wallbox Lösungen, passend für Ihr Fahrzeug und Ihre Bedürfnisse</li>
        <li>Installation inkl. aller notwendigen Materialien und Tätigkeiten (Durchbrüche, Erdarbeiten, etc.)</li>
        <li>Inbetriebnahme und Einweisung in die Ladetechnik</li>
        <li>Jährlich technische Wartung nach DGUV3</li>
        <li>Reparaturservice, unter Berücksichtigung der geltenden Garantie Ansprüche</li>
      </ul>
    </article>
    <article class="card municipal">
      <div class="card-head">als Kommune</div>
      <ul class="features">
        <li>Konzeptionierung möglicher Ladeinfrastrukturen innerhalb Ihrer Gemeinde</li>
        <li>Planung und Projektsteuerung inkl. sämtlicher behördlicher Genehmigungsverfahren und Beantragung von Fördermitteln</li>
        <li>Fachgerechte Installation und Inbetriebnahme</li>
        <li>Regelmäßige Wartung gemäß Vorschrift</li>
        <li>Reparatur und Kundenservice</li>
        <li>Direkte Abrechnung mit dem Nutzer</li>
        <li>Beteiligung der Gemeinde am Umsatz</li>
        <li>Möglichkeit der Integration von Bonusprogrammen, mit denen der lokale Einzelhandel beworben wird</li>
      </ul>
    </article>
  </div>
</section>

<footer class="site-footer">
  <div class="footer-brand"><span class="brand-dot"></span>vorn-werk.de</div>
  <div class="footer-right">
    <div class="socials" aria-label="Social Media"><span></span><span></span><span></span></div>
    <nav class="footer-nav"><span>AGB</span><span>Datenschutzerklarung</span><span>Impressum</span><span>Kontakt</span><span>Karriere</span><span>FAQs</span></nav>
  </div>
</footer>
<div class="copyright">©vorn-werk GmbH</div>
</body>
</html>
```